Dental Business Card

I need Dental oriented business cards.
On the front side -
- on the first line, my name:
Dr Marlow Tasker
- on the second line (just underneath):
Doctor of Dental Medicine
- on the third line, or underneath that or in a corner, I would like the address and phone number:
5192 Ch. Birchfield
Montreal QC H2P 4K8
514-629-5074
- other than that i would maybe like a logo of a tooth, but i want it to be subtle and very basic!
- I would like the card to be preferably black or dark grey-ish with the writing in white
On the other side -
- 2-3 lines with the possibility to write the next appointment the box with the lines should be white, with the rest of the card being black

```html
<!DOCTYPE html>
<html lang="en">
<head>
<meta charset="UTF-8">
<title>Dr Marlow Tasker – Business Card</title>
<link href="https://fonts.googleapis.com/css2?family=Tinos:wght@400;700&display=swap" rel="stylesheet">
<style>
  :root {
    --backdrop: #161616;
    --card: #454545;
    --ink: #ffffff;
    --ink-soft: #e6e6e6;
    --emblem: #4d4d4d;
    --dots: #d8d8d8;
  }
  * { margin: 0; padding: 0; box-sizing: border-box; }
  html, body {
    width: 1200px; height: 900px; overflow: hidden;
    background: var(--backdrop);
    font-family: "Tinos", "Times New Roman", serif;
  }
  .canvas {
    position: relative; width: 1200px; height: 900px;
    display: flex; flex-direction: column; align-items: center; justify-content: center; gap: 40px;
  }
  .card {
    position: relative; width: 700px; height: 400px;
    background: var(--card); color: var(--ink);
    box-shadow: 0 8px 24px rgba(0,0,0,.6);
    overflow: hidden;
  }
  .emblem {
    position: absolute; background: var(--emblem); border-radius: 40% 40% 30% 30%;
  }
  /* appointment side */
  .appointment .emblem { left: 245px; top: 40px; width: 210px; height: 300px; opacity: .7; }
  .appointment-title {
    position: absolute; top: 118px; width: 100%; text-align: center;
    font-weight: 700; font-size: 26px; letter-spacing: .5px;
  }
  .appointment-fields {
    position: absolute; left: 60px; right: 70px; top: 185px;
    list-style: none; display: flex; flex-direction: column; gap: 22px;
  }
  .field { display: flex; align-items: flex-end; gap: 20px; font-size: 20px; color: var(--ink-soft); }
  .field-label { width: 60px; }
  .field-line { flex: 1; border-bottom: 1px dashed var(--dots); height: 1px; margin-bottom: 4px; }
  /* identity side */
  .identity .emblem { left: 445px; top: 95px; width: 225px; height: 270px; }
  .identity-block { position: absolute; left: 55px; top: 178px; }
  .doctor-name { font-weight: 700; font-size: 40px; line-height: 1; }
  .doctor-title { font-size: 22px; color: var(--ink-soft); margin-top: 8px; }
  .divider { width: 200px; height: 1px; background: var(--ink-soft); margin: 14px 0 18px; }
  .contact { list-style: none; font-size: 20px; color: var(--ink-soft); line-height: 1.6; }
  .contact-key { display: inline-block; width: 22px; font-size: 22px; }
</style>
</head>
<body>
<main class="canvas">
  <section class="card appointment" aria-label="Appointment side">
    <div class="emblem" role="img" aria-label="Subtle tooth emblem"></div>
    <h2 class="appointment-title">APPOINTMENT</h2>
    <ul class="appointment-fields">
      <li class="field"><span class="field-label">For:</span><span class="field-line"></span></li>
      <li class="field"><span class="field-label">Date:</span><span class="field-line"></span></li>
      <li class="field"><span class="field-label">Time:</span><span class="field-line"></span></li>
    </ul>
  </section>

  <section class="card identity" aria-label="Identity side">
    <div class="emblem" role="img" aria-label="Subtle embossed tooth emblem"></div>
    <div class="identity-block">
      <h1 class="doctor-name">Dr Marlow Tasker</h1>
      <p class="doctor-title">Doctor of Dental Medicine</p>
      <div class="divider"></div>
      <ul class="contact">
        <li><span class="contact-key">P</span> : 514-629-5074</li>
        <li><span class="contact-key">A</span> : 5192 Ch. Birchfield Montreal QC H2P 4K8</li>
      </ul>
    </div>
  </section>
</main>
</body>
</html>
```